Velmorytrips.com web design project + logo design

Hi,

We are a Russian online tour operator - roamquiltex.com

We are looking to tranmsfer our domain to velmorytrips.com. The website and logo need to be velmoryesque - we are not looking to change our functionality, but we need to make the website much more attracitve to clients, much more wild looking but at the same time remaining a professional travel company.

The main concept of the website should be innovative travel (as velmory was an innovator). Alternatively, you could go down the artist route and go down the draw / design your own tour road.

On our website the customer is able to combine travel services (hotels, flights, Visa services, and soon chauffeur, car rental etc...) put it into their basket (the basket definitely has to look better than it is at the moment) and pay for it in one go by card.

We are also stressin our customer support with web chat, call centre etc... (call centre number at the top of the page)

We aim to provide an easy user experience, but we need to make it have some more style, so I will be waiting for what you guys can come up with.
Let me know if you have any questions - skype is: mrkostelin

Industry/Entity Type

It Company

Logo Text

Requirements
Must have
• It is quite a simple task - to take the existing website roamquiltex.com and velmorysize it to create velmorytrips.com, the functionality of the website will remain the same and there are not many pages in the website. Homepage, Checkout step1, Checkout step 2 (you can view both of these if you select a service) and the generic pages for T&C''s, Privacy policy etc...

IMPORTANT UPDATE

We are also looking at how the search results will look in the designs, (please do a search on our website for hotel / flight)

```html
<!DOCTYPE html>
<html lang="en">
<head>
<meta charset="utf-8">
<title>Velmorytrips.com — A Professional Travel Company</title>
<link rel="stylesheet" href="https://fonts.googleapis.com/css2?family=Open+Sans:wght@300;400;600;700;800&display=swap">
<style>
:root{
  --sky-top:#1d4fa8;
  --sky-mid:#5f8fcf;
  --city:#6e7378;
  --panel:rgba(52,56,64,.86);
  --panel-head-top:#ffffff;
  --panel-head-bottom:#d9dbe0;
  --head-text:#4a4f57;
  --brand-blue:#2450b8;
  --muted:#9aa0a8;
  --white:#ffffff;
  --nav:#3d424b;
  --ink:#222;
}
*{box-sizing:border-box;margin:0;padding:0}
html,body{width:1200px;height:754px;overflow:hidden}
body{position:relative;font-family:"Open Sans",Arial,sans-serif;color:var(--white);background:var(--sky-mid)}
.backdrop{position:absolute;inset:0;background:linear-gradient(180deg,var(--sky-top) 0%,#3f73c2 30%,#9fb6d2 55%,var(--city) 75%,#4a4e54 100%)}
.abs{position:absolute}

.utility{top:8px;font-size:12px;color:var(--white)}
.utility.left{left:161px}
.utility.right{right:171px}
.caret{display:inline-block;width:0;height:0;border-left:5px solid transparent;border-right:5px solid transparent;border-top:6px solid var(--white);margin:0 6px 1px 4px;vertical-align:middle}

.masthead{left:135px;top:33px;width:919px;height:94px;background:linear-gradient(#fff,#eef0f3);border:1px solid #d3d6db}
.logo{position:absolute;left:33px;top:28px;font-weight:800;font-size:30px;letter-spacing:.5px;color:var(--brand-blue);line-height:1}
.logo small{font-size:11px;font-weight:800}
.tagline{position:absolute;left:34px;top:64px;font-size:10px;letter-spacing:3.6px;color:var(--muted);font-weight:600}
.social{position:absolute;right:24px;top:14px;display:flex;gap:5px}
.social span{width:23px;height:23px;border-radius:5px;background:#8a96a8}

.nav{left:135px;top:127px;width:919px;height:50px;background:linear-gradient(#484d56,var(--nav));display:flex;align-items:center;padding-left:26px}
.nav a{color:var(--white);text-decoration:none;font-weight:300;font-size:16px;letter-spacing:.6px;margin-right:29px}
.search{position:absolute;right:26px;top:12px;width:149px;height:25px;border-radius:13px;background:#eceef1;color:#555;font-size:13px;padding:3px 12px}
.search svg{position:absolute;right:4px;top:3px}

.panel{background:var(--panel)}
.panel-head{height:35px;background:linear-gradient(var(--panel-head-top),var(--panel-head-bottom));color:var(--head-text);font-size:13px;letter-spacing:.6px;padding:10px 26px}
.label{font-size:13px;color:var(--white)}
.select{width:105px;height:22px;background:#fff;color:var(--ink);font-size:12px;padding:2px 5px;position:absolute}
.select svg{position:absolute;right:4px;top:5px}
.more{font-size:13px}
.pill{height:27px;border-radius:14px;background:linear-gradient(#fff,#dcdfe3);color:var(--ink);font-size:13px;text-align:center;line-height:27px;width:131px}

.plan{left:135px;top:189px;width:449px;height:151px}
.powered{left:135px;top:352px;width:449px;height:143px}
.brand-word{color:var(--brand-blue);font-weight:700;font-size:15px;letter-spacing:0;margin-left:6px}
.radio{display:inline-block;width:14px;height:14px;border-radius:50%;background:#e4e6ea;vertical-align:-2px;margin-right:9px}
.radio.on{box-shadow:inset 0 0 0 4px #e4e6ea;background:#555}

.why{left:604px;top:189px;width:450px;height:321px}
.checks{list-style:none;position:absolute;left:26px;top:48px}
.checks li{height:36px;display:flex;align-items:center;font-weight:800;font-size:15px;letter-spacing:.8px}
.checks .box{width:26px;height:26px;border-radius:4px;background:linear-gradient(#fff,#cfd2d6);margin-right:13px;display:flex;align-items:center;justify-content:center}

.deals{left:135px;top:510px;width:919px;height:180px}
.deal{position:absolute;top:45px;width:127px;height:125px}
.deal .caption{position:absolute;left:0;right:0;bottom:0;height:34px;background:rgba(25,60,90,.55);font-size:13px;padding:9px 8px;letter-spacing:.4px}

.footer{left:135px;top:690px;width:919px;height:64px;background:rgba(60,63,68,.88)}
.to-top{position:absolute;left:26px;top:27px;font-size:13px;letter-spacing:.4px}
.to-top svg{vertical-align:0;margin-right:9px}
.rights{position:absolute;right:14px;top:26px;height:21px;border:1.5px solid var(--white);border-radius:11px;font-size:10.5px;font-weight:700;padding:2px 11px;letter-spacing:.2px}
</style>
</head>
<body>
<div class="backdrop" role="img" aria-label="City skyline and waterfront under a deep blue sky with white clouds"></div>

<div class="abs utility left">USD ($)<span class="caret"></span> | &nbsp;English (US)<span class="caret"></span></div>
<div class="abs utility right">Sign in &nbsp;| &nbsp;Sign up &nbsp;| &nbsp;Help</div>

<header class="abs masthead">
  <div class="logo">VELMORYTRIPS<small>.COM</small></div>
  <div class="tagline">A PROFESSIONAL TRAVEL COMPANY</div>
  <div class="social" aria-label="Social links"><span></span><span></span><span></span><span></span></div>
</header>

<nav class="abs nav">
  <a href="#">HOME</a><a href="#">ABOUT</a><a href="#">SERVICES</a><a href="#">LOCATIONS</a><a href="#">AFFILIATES</a><a href="#">CONTACT</a>
  <div class="search">Search
    <svg width="28" height="19" viewBox="0 0 28 19"><rect width="28" height="19" rx="9.5" fill="#fff"/><circle cx="13" cy="8.5" r="3.5" fill="none" stroke="#999" stroke-width="1.5"/><line x1="15.5" y1="11" x2="18" y2="13.5" stroke="#999" stroke-width="1.5"/></svg>
  </div>
</nav>

<section class="abs panel plan">
  <div class="panel-head">PLAN YOUR TRIP</div>
  <div class="abs label" style="left:37px;top:53px">Select a country</div>
  <div class="abs label" style="left:179px;top:53px">Select a city</div>
  <div class="abs label" style="left:309px;top:53px">Select a hotel</div>
  <div class="select" style="left:38px;top:68px">Drop-Down<svg width="8" height="12"><path d="M1 5L4 1L7 5ZM1 7L4 11L7 7Z" fill="#333"/></svg></div>
  <div class="select" style="left:176px;top:68px">Drop-Down<svg width="8" height="12"><path d="M1 5L4 1L7 5ZM1 7L4 11L7 7Z" fill="#333"/></svg></div>
  <div class="select" style="left:308px;top:68px">Drop-Down<svg width="8" height="12"><path d="M1 5L4 1L7 5ZM1 7L4 11L7 7Z" fill="#333"/></svg></div>
  <div class="abs more" style="left:43px;top:113px">Show Additional Options<span class="caret" style="margin-left:9px"></span></div>
  <div class="abs pill" style="left:281px;top:109px">Plan it for me</div>
</section>

<section class="abs panel powered">
  <div class="panel-head">POWERED BY <span class="brand-word">Voyantra</span></div>
  <div class="abs label" style="left:38px;top:62px"><span class="radio on"></span>Book a hotel</div>
  <div class="abs label" style="left:175px;top:62px"><span class="radio"></span>Book a flight</div>
  <div class="abs more" style="left:42px;top:104px">Show Additional Options<span class="caret" style="margin-left:9px"></span></div>
  <div class="abs pill" style="left:281px;top:92px">Submit</div>
</section>

<section class="abs panel why">
  <div class="panel-head">WHY HOTEL RIDEWELL.COM ?</div>
  <ul class="checks">
    <li><span class="box"><svg width="16" height="14"><path d="M1 7L6 12L15 1" fill="none" stroke="#8d9196" stroke-width="2.5"/></svg></span>ALL INCLUSIVE PRICING</li>
    <li><span class="box"><svg width="16" height="14"><path d="M1 7L6 12L15 1" fill="none" stroke="#8d9196" stroke-width="2.5"/></svg></span>FEE CANCELS UPTO TWO HOURS OUT</li>
    <li><span class="box"><svg width="16" height="14"><path d="M1 7L6 12L15 1" fill="none" stroke="#8d9196" stroke-width="2.5"/></svg></span>CLIENT ASSISTANCE 24/7/365</li>
    <li><span class="box"><svg width="16" height="14"><path d="M1 7L6 12L15 1" fill="none" stroke="#8d9196" stroke-width="2.5"/></svg></span>ON TIME GUARUNTEE</li>
    <li><span class="box"><svg width="16" height="14"><path d="M1 7L6 12L15 1" fill="none" stroke="#8d9196" stroke-width="2.5"/></svg></span>ALL INCLUSIVE PRICING</li>
    <li><span class="box"><svg width="16" height="14"><path d="M1 7L6 12L15 1" fill="none" stroke="#8d9196" stroke-width="2.5"/></svg></span>FEE CANCELS UPTO TWO HOURS OUT</li>
    <li><span class="box"><svg width="16" height="14"><path d="M1 7L6 12L15 1" fill="none" stroke="#8d9196" stroke-width="2.5"/></svg></span>CLIENT ASSISTANCE 24/7/365</li>
  </ul>
</section>

<section class="abs panel deals">
  <div class="panel-head">TOP DEALS</div>
  <div class="deal" style="left:22px;background:linear-gradient(#4fa3dd,#dfe9f1 60%,#2c6a9e)" role="img" aria-label="White cruise ship at sea"><div class="caption">Cruise Trip</div></div>
  <div class="deal" style="left:171px;background:linear-gradient(#1f7fd0,#7cbde6 55%,#3e7a2e)" role="img" aria-label="Palm trees against a blue sky"><div class="caption">Srilankan Palms</div></div>
  <div class="deal" style="left:321px;background:radial-gradient(circle at 50% 45%,#f2c230,#c78a16 35%,#2f8f8c 70%)" role="img" aria-label="Stack of gold casino chips"><div class="caption">Visit Vegas</div></div>
  <div class="deal" style="left:470px;background:linear-gradient(#e25a12,#5a2a2a 30%,#1d1a2a 60%,#3a2a14)" role="img" aria-label="City lights at dusk"><div class="caption">Happening Seoul</div></div>
  <div class="deal" style="left:620px;background:linear-gradient(#7fb8e8,#c9dff0 45%,#e6e24a 75%,#5a9ec0)" role="img" aria-label="Swimmer with a yellow float at the beach"><div class="caption">Hawaiian Beach</div></div>
  <div class="deal" style="left:770px;background:linear-gradient(#2f7fd6,#9fd0ec 50%,#e8e4da)" role="img" aria-label="Thatched beach umbrella and loungers on white sand"><div class="caption">Blue Mauritius</div></div>
</section>

<footer class="abs footer">
  <div class="to-top"><svg width="11" height="7"><path d="M0 7L5.5 0L11 7Z" fill="#fff"/></svg>Back to top</div>
  <div class="rights">VELMORYTRIPS.COM &nbsp;| ALL RIGHT RESERVE</div>
</footer>
</body>
</html>
```